Need a creative cover photo for social media profiles

We are rebranding and would like to promote the new look on our cover image for our social platforms (LinkedIn, Facebook, Twitter). It should feel similar in brand as the attached collateral. We want this to make a statement as our new logo and feel are completely different from where we currently are. I am sending along examples of other collateral we have created.
Target Market(s)
IT, accounting professionals and companies looking to hire those professionals.
Industry/Entity Type
Staffing
Requirements
Must have
- Logo
Our corporate font is Nexa Bold for headlines and Ebrima for content.
CMYK combinations for our corporate colors
C 2. M 66, Y 87, K 0
C 84, M 69, Y 47, K 39

```html
<!DOCTYPE html>
<html lang="en">
<head>
<meta charset="utf-8">
<title>Vantora Group – Social Cover</title>
<link href="https://fonts.googleapis.com/css2?family=Montserrat:wght@400;700;800&family=Hind:wght@400;500&display=swap" rel="stylesheet">
<style>
  :root {
    --brand-orange: #ec7a3a;
    --brand-navy: #2f3d52;
    --photo-dark: #b9541f;
    --photo-light: #f3b27e;
    --paper: #ffffff;
    --stage: #ebebeb;
  }
  html, body {
    margin: 0;
    width: 1200px;
    height: 1200px;
    overflow: hidden;
    background: var(--stage);
  }
  .cover-frame {
    position: absolute;
    left: 30px;
    top: 389px;
    width: 1270px;
    height: 470px;
    transform: scale(0.8976);
    transform-origin: 0 0;
    box-shadow: 0 4px 14px rgba(0,0,0,0.25);
    background: var(--paper);
  }
  .cover-shapes {
    position: absolute;
    inset: 0;
    width: 1270px;
    height: 470px;
  }
  .brand-mark {
    position: absolute;
    left: 188px;
    top: 32px;
    width: 76px;
    height: 76px;
    border-radius: 50%;
    background: var(--brand-orange);
  }
  .brand-name {
    position: absolute;
    left: 0;
    width: 452px;
    top: 124px;
    margin: 0;
    text-align: center;
    font: 800 39px/1 "Montserrat", sans-serif;
    letter-spacing: 3px;
    color: var(--brand-navy);
  }
  .headline {
    position: absolute;
    left: 0;
    width: 452px;
    top: 182px;
    margin: 0;
    text-align: center;
    font: 400 42px/46px "Montserrat", sans-serif;
    color: var(--brand-orange);
  }
  .headline .line-2 { font-size: 45px; }
  .services-pill {
    position: absolute;
    left: 74px;
    top: 281px;
    width: 305px;
    height: 38px;
    border-radius: 19px;
    background: var(--brand-navy);
    color: var(--brand-orange);
    text-align: center;
    font: 700 28px/38px "Montserrat", sans-serif;
  }
  .services-list {
    position: absolute;
    left: 56px;
    top: 322px;
    margin: 0;
    padding: 0;
    list-style: none;
    color: var(--paper);
    font: 500 24px/1 "Hind", sans-serif;
  }
  .services-list li {
    display: flex;
    align-items: center;
    gap: 22px;
    height: 39px;
  }
  .services-list svg { width: 24px; height: 24px; }
  .site-link {
    position: absolute;
    left: 678px;
    top: 384px;
    display: flex;
    align-items: center;
    gap: 14px;
    color: var(--paper);
    font: 500 33px/1 "Hind", sans-serif;
  }
  .site-link svg { width: 36px; height: 36px; }
</style>
</head>
<body>
  <section class="cover-frame">
    <svg class="cover-shapes" viewBox="0 0 1270 470" aria-hidden="false">
      <defs>
        <linearGradient id="photoTone" x1="0" y1="0" x2="1" y2="1">
          <stop offset="0" stop-color="var(--photo-light)"/>
          <stop offset="0.5" stop-color="#e08448"/>
          <stop offset="1" stop-color="var(--photo-dark)"/>
        </linearGradient>
      </defs>
      <rect class="services-panel" x="0" y="280" width="520" height="190" fill="var(--brand-orange)"/>
      <polygon class="divider-navy" points="478,0 490,0 435,235 502,470 490,470 423,235" fill="var(--brand-navy)"/>
      <polygon class="divider-orange" points="490,0 502,0 447,235 514,470 502,470 435,235" fill="var(--brand-orange)"/>
      <polygon class="team-photo" role="img" aria-label="Photo of four colleagues gathered around a tablet in a bright office, warm orange tint"
               points="502,0 1270,0 1270,360 482,360 447,235" fill="url(#photoTone)"/>
      <polygon class="web-band" points="482,360 1270,360 1270,470 514,470" fill="var(--brand-navy)"/>
    </svg>

    <div class="brand-mark" aria-hidden="true"></div>
    <h1 class="brand-name">VANTORA GROUP</h1>
    <h2 class="headline"><span>SPECIALIZED</span><br><span class="line-2">IT SOLUTIONS</span></h2>

    <div class="services-pill">OUR SERVICES</div>
    <ul class="services-list">
      <li><svg viewBox="0 0 24 24"><rect x="2" y="4" width="17" height="17" fill="none" stroke="#fff" stroke-width="2.2"/><path d="M6 12l4 4 11-12" fill="none" stroke="#fff" stroke-width="2.6"/></svg>Accounting &amp; Finance</li>
      <li><svg viewBox="0 0 24 24"><rect x="2" y="4" width="17" height="17" fill="none" stroke="#fff" stroke-width="2.2"/><path d="M6 12l4 4 11-12" fill="none" stroke="#fff" stroke-width="2.6"/></svg>IT &amp; Healthcare</li>
      <li><svg viewBox="0 0 24 24"><rect x="2" y="4" width="17" height="17" fill="none" stroke="#fff" stroke-width="2.2"/><path d="M6 12l4 4 11-12" fill="none" stroke="#fff" stroke-width="2.6"/></svg>IT Staffing</li>
    </ul>

    <div class="site-link">
      <svg viewBox="0 0 36 36" aria-hidden="true">
        <g fill="none" stroke="var(--brand-orange)" stroke-width="2.4">
          <circle cx="18" cy="18" r="15"/>
          <ellipse cx="18" cy="18" rx="7" ry="15"/>
          <line x1="3" y1="18" x2="33" y2="18"/>
          <line x1="6" y1="10" x2="30" y2="10"/>
          <line x1="6" y1="26" x2="30" y2="26"/>
        </g>
      </svg>
      <span>www.vantoragroup.com</span>
    </div>
  </section>
</body>
</html>
```